an author seeking a cool ebook cover design

We need an ebook cover design for an old book I'd written 10yrs ago so that I can make it into an ebook. It's a self help health and wellbeing book, that covers everything from fitness, nutrition to mediation and stress management.

I'd like to see designs that use a toolbox (i have attached a photo I'd like to use (no need for stock photo as it's my toolbox and photo).

The cover should be clear and easy to read.

here's a description of what's inside the book (i've also attached a rough pdf of insides)
Marrow Quiet Ledger is full of all the practical tips you need to help get you thinking straight, feeling great and looking great.

This concise books saves you time by finding the right tool you need for your own personal challenge, be it physical, mental or energetic. It’s practical, fun, easy to read and most of all it’s effective.

Arto Pimbley brings all his experience and knowledge and bundles it all together to give you a book that is in many ways the ‘evening almanac’ on lifestyle! It will help you turn every day dramas and challenges into remarkable successes.

The three main parts to this book are essential to living: The mind, the body and the spirit. You will learn how to meditate, stretch, exercise, eat well to live longer, choose a new direction in life, deal with stress, use acupressure for illness and learn how to clear a cluttered mind and transform it into a happy and content one.

Target Market(s)

25- 40yr old mostly female

Industry/Entity Type

Nutrition

Requirements
Must have
• must have:
the author name - Arto Pimbley
Book title - Marrow Quiet Ledger
bi line - quick tips for a happier healthier you
picture of toolbox
must have specs:

1,600 pixels wide by 2,400 pixels tall or similar ratio. The image must be at least 1,600 pixels wide, and the height should be greater than the width.
image must be in RGB color, not CMYK
file type to be jpeg - maximum file size 18MB
Nice to have
• like to see more of hand written font style like 'sketch nice' if possible

```html
<!DOCTYPE html>
<html lang="en">
<head>
<meta charset="UTF-8">
<title>Marrow Quiet Ledger — ebook cover</title>
<link href="https://fonts.googleapis.com/css2?family=Cabin+Sketch:wght@700&family=Special+Elite&family=Source+Sans+3:wght@700&display=swap" rel="stylesheet">
<style>
  :root {
    --paper: #ffffff;
    --edge: #d9d9d9;
    --title-red: #e0231c;
    --ink: #2b2b2b;
    --author-grey: #4a4a4a;
    --box-light: #d8382e;
    --box-mid: #b8231c;
    --box-dark: #7e1410;
  }
  html, body {
    margin: 0;
    padding: 0;
    width: 800px;
    height: 1200px;
    overflow: hidden;
    background: var(--paper);
  }
  .cover {
    position: relative;
    width: 800px;
    height: 1200px;
    box-sizing: border-box;
    border: 2px solid var(--edge);
    background: var(--paper);
  }
  .book-title {
    position: absolute;
    top: 70px;
    left: 0;
    width: 100%;
    margin: 0;
    display: flex;
    flex-direction: column;
    align-items: center;
    font-family: "Cabin Sketch", cursive;
    font-weight: 700;
    color: var(--title-red);
    line-height: 0.98;
    text-align: center;
  }
  .book-title .line-one { font-size: 136px; }
  .book-title .line-two { font-size: 140px; }
  .book-title .line-three { font-size: 158px; }
  .byline {
    position: absolute;
    top: 528px;
    left: 0;
    width: 100%;
    margin: 0;
    text-align: center;
    font-family: "Special Elite", monospace;
    font-size: 27px;
    color: var(--ink);
    letter-spacing: 0.5px;
  }
  .toolbox-photo {
    position: absolute;
    left: 160px;
    top: 662px;
    width: 494px;
    height: 336px;
    border-radius: 14px;
    background: linear-gradient(180deg, var(--box-light) 0%, var(--box-mid) 55%, var(--box-dark) 100%);
  }
  .author {
    position: absolute;
    top: 1092px;
    left: 0;
    width: 100%;
    margin: 0;
    text-align: center;
    font-family: "Source Sans 3", sans-serif;
    font-weight: 700;
    font-size: 44px;
    color: var(--author-grey);
  }
</style>
</head>
<body>
  <main class="cover">
    <h1 class="book-title">
      <span class="line-one">Marrow</span>
      <span class="line-two">Quiet</span>
      <span class="line-three">Ledger</span>
    </h1>
    <p class="byline">quick tips for a happier healthier you</p>
    <div class="toolbox-photo" role="img" aria-label="Photograph of a worn red metal toolbox with its lid slightly open"></div>
    <p class="author">Arto Pimbley</p>
  </main>
</body>
</html>
```